Acrylic print memorial plaque for entrance

I need a design for an acrylic print in DIN A0 portrait format or 1.5x DIN A0.

The top 40% should contain the lettering "Veronika's Meadow Haven." The lettering should frame three pictures. In the center is a portrait of Vero (Veronika), with "In Memoriam" below the name and the dates *November 20, 1980 †May 15, 2024. The head of the horse Solvina should be placed on the left, and Bellis's head on the right.
The next 35% of the area should depict the portraits of Gerhard (left), Henrik (middle), and Frieda (right) in the upper part. Each with their name underneath. The lower part of this 35% should contain

“Our helpers:”
Then the portraits of Dieter, Helene, Uschi & Glenn should be taken in the following order. Each one should also have its name underneath the portrait.
The remaining 25% should contain the following:
“We would like to thank:
Klaus & Ingrid for their valuable support, and Hanni for her help and tips on handling the horse. We would also like to thank the Weibel family, especially Beni & Sabine and Flori & Greta, for allowing us to create this paradise according to our ideas and for the construction. And, of course, the many other helpers and supporters.
The images should be isolated as much as possible and scaled to fit the print size. If possible, only the faces (head + neck) should be included.

Cut out, shape, or mirror the horse heads depending on the design.

The various images can be used as backgrounds, provided the design allows it.

Target Market(s)

No target mark, memorial plaque for the stable

Font styles to use
Serif
Decorative
Script

Requirements
Must have
• Honest, Authentic, Devotional
Should not have
• Kitsch, too playful.

```html
<!DOCTYPE html>
<html lang="en">
<head>
<meta charset="utf-8">
<title>Veronika's Meadow Haven – Memorial Plaque</title>
<link href="https://fonts.googleapis.com/css2?family=Dancing+Script:wght@500;600&family=Della+Respira&display=swap" rel="stylesheet">
<style>
  :root {
    --paper: #efe5dc;
    --paper-deep: #e2d5c9;
    --sand: #d9cabd;
    --ink: #3d3029;
    --ink-soft: #4a3b33;
    --photo-warm: #b49a86;
    --photo-dark: #3b302b;
    --photo-chestnut: #9a5a36;
    --photo-skin: #c9a48e;
  }
  * { margin: 0; padding: 0; box-sizing: border-box; }
  html, body { width: 849px; height: 1200px; overflow: hidden; background: var(--paper); }
  .plaque {
    position: relative;
    width: 849px;
    height: 1200px;
    overflow: hidden;
    color: var(--ink);
    font-family: "Della Respira", Georgia, serif;
  }
  .backdrop {
    position: absolute; inset: 0;
    background:
      linear-gradient(180deg, var(--paper) 0%, #ebe0d6 40%, #e3d6ca 62%, var(--sand) 100%);
  }
  .backdrop::after {
    content: ""; position: absolute; left: 0; right: 0; top: 520px; height: 180px;
    background: linear-gradient(180deg, rgba(210,196,184,0) 0%, rgba(200,186,173,.35) 60%, rgba(215,202,190,0) 100%);
  }
  .title {
    position: absolute; left: 0; right: 0; top: 14px;
    text-align: center;
    font-family: "Dancing Script", cursive;
    font-weight: 600;
    font-size: 74px;
    line-height: 1;
    color: var(--ink);
    letter-spacing: 1px;
  }
  .photo {
    position: absolute;
    box-shadow: 0 0 14px 6px rgba(239,229,220,.9) inset;
  }
  .photo--brushed { border-radius: 10px 22px 8px 18px; }
  .photo--framed { border-radius: 6px; }
  .horse-left { left: 28px; top: 135px; width: 264px; height: 182px;
    background: radial-gradient(ellipse at 55% 55%, var(--photo-dark) 0%, #5d5049 55%, #a69a90 100%); }
  .horse-right { left: 580px; top: 132px; width: 228px; height: 167px;
    background: radial-gradient(ellipse at 45% 50%, var(--photo-chestnut) 0%, #8a6a55 55%, #8f877f 100%); }
  .portrait-main { left: 324px; top: 114px; width: 217px; height: 270px;
    background: radial-gradient(ellipse at 50% 45%, var(--photo-skin) 0%, #8d7464 55%, #cfc6be 100%); }
  .portrait-family, .portrait-helper {
    background: radial-gradient(ellipse at 50% 42%, var(--photo-skin) 0%, var(--photo-warm) 50%, #d8cdc3 100%);
  }
  .fam-left { left: 107px; top: 454px; width: 153px; height: 217px; }
  .fam-mid { left: 352px; top: 530px; width: 157px; height: 182px; }
  .fam-right { left: 597px; top: 454px; width: 152px; height: 217px; }
  .help-1 { left: 78px; top: 812px; width: 116px; height: 169px; }
  .help-2 { left: 271px; top: 812px; width: 116px; height: 169px; }
  .help-3 { left: 463px; top: 812px; width: 116px; height: 169px; }
  .help-4 { left: 655px; top: 812px; width: 116px; height: 169px; }

  .memorial { position: absolute; left: 0; right: 0; top: 392px; text-align: center; }
  .memorial-name { font-size: 44px; line-height: 1; color: var(--ink); }
  .memorial-line { font-family: "Dancing Script", cursive; font-weight: 600; font-size: 31px; line-height: 1; margin-top: 2px; }
  .memorial-dates { font-size: 17px; margin-top: 6px; color: var(--ink-soft); }

  .name-label {
    position: absolute; text-align: center; font-size: 29px; line-height: 1; color: var(--ink);
  }
  .name-label--small { font-size: 25px; }

  .section-heading {
    position: absolute;
    font-family: "Dancing Script", cursive;
    font-weight: 600;
    font-size: 35px;
    line-height: 1;
    color: var(--ink);
    padding-bottom: 3px;
    border-bottom: 2px solid var(--ink);
  }
  .helpers-heading { left: 80px; top: 751px; }
  .thanks-heading { left: 57px; top: 1032px; }

  .thanks-text {
    position: absolute; left: 40px; right: 40px; top: 1074px;
    text-align: center; font-size: 19.5px; line-height: 24px; color: var(--ink);
  }
</style>
</head>
<body>
<main class="plaque">
  <div class="backdrop" role="img" aria-label="Faded photograph of the sandy riding paddock with fences and a light pole"></div>

  <h1 class="title">Veronika's Meadow Haven</h1>

  <div class="photo photo--brushed horse-left" role="img" aria-label="Head of the dark horse Solvina"></div>
  <div class="photo photo--brushed portrait-main" role="img" aria-label="Portrait of Veronika"></div>
  <div class="photo photo--brushed horse-right" role="img" aria-label="Head of the chestnut horse Bellis"></div>

  <section class="memorial">
    <p class="memorial-name">Veronika</p>
    <p class="memorial-line">In Memoriam</p>
    <p class="memorial-dates">November 20, 1980 † May 15, 2024</p>
  </section>

  <div class="photo photo--framed portrait-family fam-left" role="img" aria-label="Portrait of Gerhard"></div>
  <div class="photo photo--brushed portrait-family fam-mid" role="img" aria-label="Portrait of Henrik"></div>
  <div class="photo photo--framed portrait-family fam-right" role="img" aria-label="Portrait of Frieda"></div>
  <p class="name-label" style="left:107px;width:153px;top:680px;">Gerhard</p>
  <p class="name-label" style="left:352px;width:157px;top:726px;">Henrik</p>
  <p class="name-label" style="left:597px;width:152px;top:680px;">Frieda</p>

  <h2 class="section-heading helpers-heading">Our helpers:</h2>
  <div class="photo photo--framed portrait-helper help-1" role="img" aria-label="Portrait of Dieter"></div>
  <div class="photo photo--framed portrait-helper help-2" role="img" aria-label="Portrait of Helene"></div>
  <div class="photo photo--framed portrait-helper help-3" role="img" aria-label="Portrait of Uschi"></div>
  <div class="photo photo--framed portrait-helper help-4" role="img" aria-label="Portrait of Glenn"></div>
  <p class="name-label name-label--small" style="left:58px;width:156px;top:988px;">Dieter</p>
  <p class="name-label name-label--small" style="left:251px;width:156px;top:988px;">Helene</p>
  <p class="name-label name-label--small" style="left:443px;width:156px;top:988px;">Uschi</p>
  <p class="name-label name-label--small" style="left:635px;width:156px;top:988px;">Glenn</p>

  <h2 class="section-heading thanks-heading">We would like to thank:</h2>
  <p class="thanks-text">Klaus &amp; Ingrid for their valuable support, and Hanni for her help and tips on handling the horse. We would also like to thank the Weibel family, especially Beni &amp; Sabine and Flori &amp; Greta, for allowing us to create this paradise according to our ideas and for the construction. And, of course, the many other helpers and supporters.</p>
</main>
</body>
</html>
```